Meridel Advisory & Coaching Collective Web Site Design

Help!

We have started designing and building a Web site to promote and sell training services to HR managers. But we are not very good designers. In fact, we stink.

We have a logo.

We have most of the content (more or less) and the site architecture. But we have put together a pretty lousy look and feel.

Take a look: http://brightlowpath.example/vortalindex.html

What we'd like is a Web 3.0 type design - clean, simple, modern looking. Some sites we admire:

pinvale.example
trelosk.example
skivorn.example
quibbledot.example
morpa.example

We have access to stock photography, some of which we've used on the site we've built so far. You can use those and others. But keep it simple.

Target Market(s)

Professional HR managers in larger companies

Requirements
Must have
• Use our logo and a color scheme based off of it. Logo file uploaded.

Need to see home page and examples of secondary pages, based on site currently online.

```html
<!DOCTYPE html>
<html lang="en">
<head>
<meta charset="utf-8">
<title>Cohort Compass — Generation Tools &amp; Training for HR Professionals</title>
<link rel="stylesheet" href="https://fonts.googleapis.com/css2?family=Questrial&family=Open+Sans:wght@700&family=Arimo:wght@400;700&display=swap">
<style>
  :root {
    --brand-blue: #0b3a9e;
    --footer-blue: #0a3596;
    --ink: #111111;
    --page-top: #f0f0f0;
    --nav-top: #ececec;
    --nav-bottom: #cfcfcf;
    --stage-top: #fbfbfb;
    --stage-bottom: #e2e2e2;
    --band-top: #f1f1f1;
    --band-bottom: #dcdcdc;
    --green-top: #62c85e;
    --green-bottom: #3a9f39;
    --orange-top: #f9a443;
    --orange-bottom: #e07815;
    --red-top: #d8403f;
    --red-bottom: #a9181d;
    --white: #ffffff;
  }
  * { margin: 0; padding: 0; box-sizing: border-box; }
  html, body { width: 1200px; height: 878px; overflow: hidden; }
  body { position: relative; background: var(--page-top); font-family: "Arimo", Arial, sans-serif; color: var(--ink); }

  .site-header { position: absolute; left: 0; top: 0; width: 1200px; height: 90px; background: var(--page-top); }
  .brand { position: absolute; left: 130px; top: 28px; display: flex; align-items: center; gap: 10px; }
  .brand-dot { width: 30px; height: 30px; border-radius: 50%; background: var(--brand-blue); }
  .brand-name { font-family: "Questrial", sans-serif; font-size: 32px; color: var(--brand-blue); letter-spacing: -0.6px; }

  .main-nav { position: absolute; left: 0; top: 90px; width: 1200px; height: 46px; background: linear-gradient(var(--nav-top), var(--nav-bottom)); }
  .main-nav a { position: absolute; top: 19px; font-family: "Questrial", sans-serif; font-size: 14px; color: var(--ink); text-decoration: none; letter-spacing: 0.3px; -webkit-text-stroke: 0.25px var(--ink); }
  .main-nav .is-current { top: 8px; left: 126px; width: 74px; height: 38px; background: var(--white); padding-top: 11px; text-align: center; }

  .stage { position: absolute; left: 0; top: 136px; width: 1200px; height: 487px; background: linear-gradient(var(--stage-top), var(--stage-bottom)); }
  .stage-title { position: absolute; left: 0; top: 24px; width: 1200px; text-align: center; font-family: "Questrial", sans-serif; font-weight: 400; font-size: 43px; color: var(--brand-blue); letter-spacing: -0.6px; }

  .card { position: absolute; top: 92px; width: 302px; height: 352px; }
  .card::after { content: ""; position: absolute; left: 10px; right: 10px; bottom: -12px; height: 12px; border-radius: 50%; background: radial-gradient(ellipse at center, rgba(0,0,0,0.22), rgba(0,0,0,0) 70%); }
  .card-head { height: 44px; border-radius: 4px 4px 0 0; padding: 11px 0 0 23px; font-family: "Open Sans", sans-serif; font-weight: 700; font-size: 18px; letter-spacing: -0.4px; color: var(--white); text-shadow: 0 1px 1px rgba(0,0,0,0.35); }
  .card-gaps .card-head { padding-left: 17px; }
  .card-strategies .card-head { padding-left: 22px; }
  .card-photo { height: 247px; }
  .card-caption { position: relative; height: 61px; padding: 9px 10px 0 23px; font-family: "Open Sans", sans-serif; font-weight: 700; font-size: 16px; letter-spacing: -0.35px; line-height: 20px; color: var(--white); text-shadow: 0 1px 1px rgba(0,0,0,0.3); }
  .card-caption svg { position: absolute; left: 0; top: 0; }
  .card-generations { left: 128px; }
  .card-gaps { left: 448px; }
  .card-strategies { left: 769px; }
  .card-generations .card-head, .card-generations .card-caption { background: linear-gradient(var(--green-top), var(--green-bottom)); }
  .card-gaps .card-head, .card-gaps .card-caption { background: linear-gradient(var(--orange-top), var(--orange-bottom)); }
  .card-strategies .card-head, .card-strategies .card-caption { background: linear-gradient(var(--red-top), var(--red-bottom)); }
  .photo-meeting { background: linear-gradient(180deg, #f4f5f7 0%, #e6e8ec 22%, #8e939d 48%, #2c3140 72%, #1d1f26 100%); }
  .photo-boardroom { background: linear-gradient(180deg, #e4e1dc 0%, #b9a89a 26%, #7a4424 55%, #5a2d16 80%, #3a2418 100%); }
  .photo-team { background: linear-gradient(180deg, #d7d5d2 0%, #b89c8a 30%, #7a5a4a 55%, #e9e8e6 85%, #cfcfcf 100%); }

  .feature-band { position: absolute; left: 0; top: 623px; width: 1200px; height: 131px; background: linear-gradient(var(--band-top), var(--band-bottom)); }
  .feature { position: absolute; top: 38px; }
  .feature-icon { position: absolute; top: 0; width: 54px; height: 56px; border-radius: 8px; }
  .feature h2 { position: absolute; top: 4px; font-family: "Questrial", sans-serif; font-weight: 400; font-size: 15px; letter-spacing: 0.3px; white-space: nowrap; -webkit-text-stroke: 0.6px var(--ink); }
  .feature p { position: absolute; top: 24px; width: 150px; font-size: 11px; line-height: 17px; white-space: nowrap; }
  .icon-resources { background: linear-gradient(#3a3a3a, #111); }
  .icon-training { background: linear-gradient(#4a4a4a, #0d0d0d); border-radius: 4px; }
  .icon-tools { background: linear-gradient(135deg, #b8bcc2, #2a7fd6); }
  .icon-discuss { background: linear-gradient(#e4e8ec, #3c9ee0); border-radius: 50%; }

  .site-footer { position: absolute; left: 0; top: 754px; width: 1200px; height: 124px; background: var(--footer-blue); color: var(--white); }
  .copyright { position: absolute; left: 126px; top: 25px; font-family: "Open Sans", sans-serif; font-weight: 700; font-size: 12.5px; letter-spacing: 0.2px; }
  .footer-nav a { position: absolute; top: 25px; font-family: "Questrial", sans-serif; font-size: 13px; color: var(--white); text-decoration: none; letter-spacing: 0.2px; }
</style>
</head>
<body>
  <header class="site-header">
    <div class="brand">
      <span class="brand-dot"></span>
      <span class="brand-name">Cohort Compass for Pelland Guild</span>
    </div>
  </header>

  <nav class="main-nav">
    <a class="is-current" href="#">HOME</a>
    <a style="left:215px" href="#">GEN 101</a>
    <a style="left:300px" href="#">GEN GAPS</a>
    <a style="left:409px" href="#">STRATEGIES</a>
    <a style="left:524px" href="#">RESOURCES</a>
    <a style="left:639px" href="#">TRAINING</a>
    <a style="left:740px" href="#">TOOLS</a>
    <a style="left:815px" href="#">DISCUSS</a>
    <a style="left:905px" href="#">ABOUT</a>
    <a style="left:988px" href="#">CONTACT</a>
  </nav>

  <main class="stage">
    <h1 class="stage-title">Generation Tools &amp; Training for HR Professionals</h1>

    <article class="card card-generations">
      <div class="card-head">GENERATIONS 101</div>
      <div class="card-photo photo-meeting" role="img" aria-label="Stock photo: a smiling senior manager in a dark suit reviewing papers with colleagues in a bright office"></div>
      <div class="card-caption">
        <svg width="14" height="61" viewBox="0 0 14 61"><polygon points="0,14 12,30 0,46" fill="rgba(255,255,255,0.25)"/></svg>
        Learn who the generations are<br>and why they matter
      </div>
    </article>

    <article class="card card-gaps">
      <div class="card-head">GENERATION GAPS</div>
      <div class="card-photo photo-boardroom" role="img" aria-label="Stock photo: overhead view of a mixed-age team meeting around a polished wooden boardroom table with laptops and papers"></div>
      <div class="card-caption">
        <svg width="14" height="61" viewBox="0 0 14 61"><polygon points="0,14 12,30 0,46" fill="rgba(255,255,255,0.25)"/></svg>
        Master the challenges created<br>by today’s generation mix
      </div>
    </article>

    <article class="card card-strategies">
      <div class="card-head">GEN STRATEGIES</div>
      <div class="card-photo photo-team" role="img" aria-label="Stock photo: a young team gathered around a desk, looking at a laptop and notes together"></div>
      <div class="card-caption">
        <svg width="14" height="61" viewBox="0 0 14 61"><polygon points="0,14 12,30 0,46" fill="rgba(255,255,255,0.25)"/></svg>
        Develop successful strategies<br>that drive your organization.
      </div>
    </article>
  </main>

  <section class="feature-band">
    <div class="feature" style="left:135px">
      <div class="feature-icon icon-resources" role="img" aria-label="Notebook icon"></div>
      <h2 style="left:68px">RESOURCES</h2>
      <p style="left:69px">Lorem ipsum dolor sit amet,<br>consectetur adipisicing elit,</p>
    </div>
    <div class="feature" style="left:367px">
      <div class="feature-icon icon-training" role="img" aria-label="Graduation cap icon" style="width:72px;height:44px;top:8px"></div>
      <h2 style="left:90px">TRAINING</h2>
      <p style="left:92px">Lorem ipsum dolor sit amet,<br>consectetur adipisicing elit,</p>
    </div>
    <div class="feature" style="left:620px">
      <div class="feature-icon icon-tools" role="img" aria-label="Wrench and screwdriver icon" style="width:46px"></div>
      <h2 style="left:58px">TOOLS</h2>
      <p style="left:60px">Lorem ipsum dolor sit amet,<br>consectetur adipisicing elit,</p>
    </div>
    <div class="feature" style="left:850px">
      <div class="feature-icon icon-discuss" role="img" aria-label="Speech bubbles icon" style="width:68px"></div>
      <h2 style="left:82px">DISCUSS</h2>
      <p style="left:83px">Lorem ipsum dolor sit amet,<br>consectetur adipisicing elit,</p>
    </div>
  </section>

  <footer class="site-footer">
    <div class="copyright">© 2011 COHORT COMPASS</div>
    <nav class="footer-nav">
      <a style="left:338px" href="#">HOME</a>
      <a style="left:393px" href="#">GEN 101</a>
      <a style="left:457px" href="#">GEN GAPS</a>
      <a style="left:544px" href="#">STRATEGIES</a>
      <a style="left:637px" href="#">RESOURCES</a>
      <a style="left:730px" href="#">TRAINING</a>
      <a style="left:809px" href="#">TOOLS</a>
      <a style="left:868px" href="#">DISCUSS</a>
      <a style="left:941px" href="#">ABOUT</a>
      <a style="left:1003px" href="#">CONTACT</a>
    </nav>
  </footer>
</body>
</html>
```